Im open to ideas.. I was thinking on my business cards aswell as my logo. a place for my name. email. phone number and abn..

ive attched a file with my business logo. which i dont love the colours.. i was think a dark background with charcoal letters so something along those colour schumes but im open to ideas..

Business

BRL Constructions

```html
<!DOCTYPE html>
<html lang="en">
<head>
<meta charset="utf-8">
<title>BRL Constructions – Business Card</title>
<link rel="stylesheet" href="https://fonts.googleapis.com/css2?family=Montserrat:wght@400;500;700;800&display=swap">
<style>
  :root {
    --backdrop: #e6e4e1;
    --card: #ffffff;
    --charcoal: #1d1d1d;
    --ink: #222222;
    --red: #e3111b;
    --rule: #333333;
  }
  * { box-sizing: border-box; margin: 0; padding: 0; }
  html, body {
    width: 1200px; height: 913px; overflow: hidden;
    background: var(--backdrop);
    font-family: "Montserrat", sans-serif;
  }
  .stage {
    width: 1200px; height: 913px;
    display: flex; align-items: center; justify-content: center;
  }
  .card {
    position: relative;
    width: 1000px; height: 572px;
    background: var(--card);
    box-shadow: 0 14px 40px rgba(0,0,0,0.18);
    overflow: hidden;
  }
  .card-edge { position: absolute; left: 0; top: 0; width: 260px; height: 572px; }
  .brand {
    position: absolute; left: 150px; top: 232px;
    display: flex; align-items: center; gap: 14px;
    color: var(--charcoal);
    font-weight: 800; font-size: 40px; letter-spacing: 1px;
  }
  .brand-mark { width: 22px; height: 22px; background: var(--charcoal); }
  .holder {
    position: absolute; right: 70px; top: 110px;
    text-align: right;
  }
  .holder-name {
    color: var(--red); font-weight: 500; font-size: 36px;
    letter-spacing: 1.5px; text-transform: uppercase; line-height: 1;
  }
  .holder-rule {
    position: absolute; right: 70px; top: 162px;
    width: 640px; height: 1px; background: var(--rule);
  }
  .holder-role {
    position: absolute; right: 70px; top: 168px;
    font-size: 16px; color: var(--ink);
  }
  .contacts {
    position: absolute; right: 70px; top: 212px;
    list-style: none; text-align: right;
    font-size: 20px; color: var(--ink); line-height: 34px;
  }
  .contacts li { display: flex; justify-content: flex-end; align-items: center; gap: 10px; }
  .contacts .label { color: var(--red); font-weight: 500; }
  .contacts .accent { color: var(--red); }
  .contacts svg { width: 16px; height: 16px; flex: none; }
  .contacts .no-icon { padding-right: 26px; }
</style>
</head>
<body>
<main class="stage">
  <article class="card">
    <svg class="card-edge" viewBox="0 0 260 572" aria-hidden="true">
      <polygon points="0,0 62,0 62,300 0,330" fill="#111111"/>
      <polygon points="0,330 62,300 120,322 240,572 0,572" fill="#e3111b"/>
    </svg>

    <div class="brand"><span class="brand-mark"></span><span>BRL Constructions</span></div>

    <div class="holder"><h1 class="holder-name">Marcus Hale</h1></div>
    <div class="holder-rule"></div>
    <p class="holder-role">Director</p>

    <ul class="contacts">
      <li class="no-icon"><span><span class="label">ABN:</span> 42 118 603 275</span></li>
      <li>+330 2718-4093
        <svg viewBox="0 0 16 16" aria-hidden="true"><path d="M4 1.5l2.2 3-1.3 1.4c.8 1.8 2.2 3.2 4 4l1.4-1.3 3 2.2-1.2 2.6C6.6 13.4 2.6 9.4 1.4 3z" fill="none" stroke="#e3111b" stroke-width="1.4" stroke-linejoin="round"/></svg>
      </li>
      <li>info@brlconstructions.com
        <svg viewBox="0 0 16 16" aria-hidden="true"><rect x="1.5" y="3.5" width="13" height="9" fill="none" stroke="#e3111b" stroke-width="1.4"/><path d="M1.5 3.5L8 9l6.5-5.5" fill="none" stroke="#e3111b" stroke-width="1.4"/></svg>
      </li>
      <li><span>www.<span class="accent">brlconstructions</span>.com</span>
        <svg viewBox="0 0 16 16" aria-hidden="true"><circle cx="8" cy="8" r="6.5" fill="none" stroke="#e3111b" stroke-width="1.4"/><ellipse cx="8" cy="8" rx="3" ry="6.5" fill="none" stroke="#e3111b" stroke-width="1.2"/><path d="M1.5 8h13" stroke="#e3111b" stroke-width="1.2"/></svg>
      </li>
    </ul>
  </article>
</main>
</body>
</html>
```